Harlan Ridge Smokehouse Jamboree's 10th ever event needs a Poster! This Non-Profit is a blast

We need a totally NEW and FUN poster design to promote our tiny Kentucky town which hosts 40,000+ people who come to meet the TV Celebrity BBQ Pitmasters - who smoke meat for their fans. It is all about Beers, Bands, BBQ + Bourbon. We are a family event with Free music all weekend long.

Target Market(s)

People who love Beer, BBQ, Bands and Bourbon

Colors
ec1f27
0555a3

Requirements
Must have
• Please only use original art.
• High energy / Fresh / Young
• Name: Harlan Ridge Smokehouse Jamboree
• 10th ever
• Sept 4+5, 2020
• Bands, Beer, BBQ + Bourbon
• Hosted by: Copperfield Hollow Distillery
• 2817 Marlow Pike Ashby, KY 40198
• $5 admission - FREE MUSIC - FREE Parking
Nice to have
• Please only use original art. Trademarked images and logos will be rejected.

```html
<!DOCTYPE html>
<html lang="en">
<head>
<meta charset="utf-8">
<title>Harlan Ridge Smokehouse Jamboree – Poster</title>
<link rel="stylesheet" href="https://fonts.googleapis.com/css2?family=Anton&family=Montserrat:wght@500;700;800;900&family=Great+Vibes&display=swap">
<style>
  :root {
    --blue-deep: #0a3f8f;
    --blue-main: #0555a3;
    --blue-bright: #1a86d6;
    --navy: #1b2f6b;
    --red: #ec1f27;
    --orange: #f39a1e;
    --orange-dark: #d9601a;
    --yellow: #ffe11a;
    --white: #ffffff;
    --sky: #2a8fd4;
    --ink: #1e1e2a;
  }
  * { box-sizing: border-box; margin: 0; padding: 0; }
  html, body { width: 846px; height: 1200px; overflow: hidden; background: var(--white); }
  .poster { position: relative; width: 846px; height: 1200px; background: var(--white); font-family: "Montserrat", sans-serif; }
  .panel {
    position: absolute; left: 22px; top: 30px; width: 802px; height: 1070px;
    background: radial-gradient(ellipse at 50% 55%, var(--blue-bright) 0%, var(--blue-main) 45%, var(--blue-deep) 100%);
    overflow: hidden;
  }
  .headline-top {
    position: absolute; top: 74px; left: 0; width: 846px; text-align: center;
    color: var(--white); font-weight: 800; font-size: 47px; letter-spacing: 0.5px;
  }
  .headline-main { position: absolute; left: 55px; top: 140px; width: 740px; height: 290px; }
  .ribbon { position: absolute; left: 55px; top: 415px; width: 740px; height: 140px; }
  .ribbon-label {
    position: absolute; left: 182px; top: 424px; width: 444px; height: 74px;
    display: flex; align-items: center; justify-content: center;
    color: var(--white); font-weight: 700; font-size: 44px; letter-spacing: 16px; padding-left: 16px;
    text-shadow: 3px 3px 0 var(--navy);
  }
  .mascot-art {
    position: absolute; left: 470px; top: 500px; width: 340px; height: 480px;
    border-radius: 48% 48% 40% 40%;
    background: linear-gradient(180deg, #f3dcc0 0%, #eccfb3 42%, #8496ad 58%, #6f829b 100%);
  }
  .flames-art {
    position: absolute; left: 22px; top: 890px; width: 802px; height: 210px;
    background: linear-gradient(180deg, rgba(255,225,26,0) 0%, var(--yellow) 30%, var(--orange) 70%, var(--orange-dark) 100%);
  }
  .edition { position: absolute; left: 66px; top: 586px; color: var(--white); }
  .edition-number { font-weight: 900; font-size: 54px; line-height: 1; text-shadow: 3px 3px 0 var(--navy); }
  .edition-tag { font-weight: 800; font-size: 31px; margin-top: 8px; text-shadow: 2px 2px 0 var(--navy); }
  .highlights { position: absolute; left: 64px; top: 700px; list-style: none; color: var(--white); font-weight: 500; font-size: 24px; line-height: 34px; }
  .highlights li { display: flex; align-items: flex-start; }
  .highlights .star { width: 22px; height: 22px; margin: 5px 10px 0 0; flex: none; fill: var(--yellow); }
  .highlights .indent { padding-left: 32px; }
  .admission {
    position: absolute; left: 64px; top: 876px; color: var(--white);
    font-weight: 800; font-size: 18px; text-shadow: 2px 2px 0 var(--navy);
  }
  .admission b { color: var(--yellow); font-weight: 900; }
  .host {
    position: absolute; left: 240px; top: 995px; width: 300px; color: var(--navy);
    font-size: 13px; line-height: 18px; font-weight: 700;
  }
  .host-label { font-weight: 800; font-size: 12px; color: var(--ink); }
  .host-name { font-weight: 900; font-size: 15px; }
  .beneficiary { position: absolute; left: 65px; top: 995px; }
  .beneficiary-label { font-weight: 800; font-size: 12px; color: var(--ink); }
  .beneficiary-name {
    margin-top: 6px; width: 150px; height: 60px; background: var(--white);
    display: flex; align-items: center; gap: 8px; padding: 0 8px;
    color: var(--navy); font-weight: 800; font-size: 15px; line-height: 1.1;
  }
  .beneficiary-name .mark { width: 14px; height: 14px; background: var(--navy); flex: none; }
  .date-badge { position: absolute; left: 553px; top: 933px; width: 232px; height: 222px; }
  .badge-town {
    position: absolute; left: 553px; top: 950px; width: 232px; text-align: center;
    font-family: "Great Vibes", cursive; font-size: 50px; color: var(--white); line-height: 1;
  }
  .badge-state {
    position: absolute; left: 553px; top: 1002px; width: 232px; text-align: center;
    color: var(--white); font-weight: 500; font-size: 12px; letter-spacing: 5px;
  }
  .badge-dates {
    position: absolute; left: 573px; top: 1020px; width: 192px; height: 30px; background: var(--white);
    display: flex; align-items: center; justify-content: center;
    color: var(--navy); font-weight: 900; font-size: 21px;
  }
  .badge-year {
    position: absolute; left: 553px; top: 1050px; width: 232px; text-align: center;
    color: var(--white); font-weight: 900; font-size: 70px; line-height: 1.1;
  }
  .footer-rule { position: absolute; left: 22px; top: 1097px; width: 531px; height: 8px; background: var(--sky); }
  .site-address {
    position: absolute; left: 60px; top: 1112px; color: var(--sky);
    font-weight: 500; font-size: 24px; letter-spacing: 3px;
  }
  .site-address b { font-weight: 900; }
</style>
</head>
<body>
<main class="poster">
  <div class="panel"></div>

  <div class="flames-art" role="img" aria-label="Illustrated orange and yellow flames rising along the bottom of the poster"></div>

  <h1 class="headline-top">HARLAN RIDGE</h1>

  <svg class="headline-main" viewBox="0 0 740 290" aria-label="Smokehouse">
    <defs>
      <linearGradient id="flame-fill" x1="0" y1="0" x2="0" y2="1">
        <stop offset="0" stop-color="#ffe11a"/>
        <stop offset="0.6" stop-color="#f7b21f"/>
        <stop offset="1" stop-color="#e8671a"/>
      </linearGradient>
    </defs>
    <text x="370" y="260" text-anchor="middle" font-family="Anton, sans-serif" font-size="230"
          textLength="700" lengthAdjust="spacingAndGlyphs"
          fill="#1b2f6b" transform="translate(10 10)">SMOKEHOUSE</text>
    <text x="370" y="260" text-anchor="middle" font-family="Anton, sans-serif" font-size="230"
          textLength="700" lengthAdjust="spacingAndGlyphs"
          fill="url(#flame-fill)" stroke="#ec1f27" stroke-width="9" paint-order="stroke">SMOKEHOUSE</text>
  </svg>

  <svg class="ribbon" viewBox="0 0 740 140" aria-hidden="true">
    <polygon points="5,45 130,45 130,125 5,125 45,85" fill="#d9601a"/>
    <polygon points="610,45 735,45 695,85 735,125 610,125" fill="#d9601a"/>
    <polygon points="130,105 127,125 150,105" fill="#8a2a10"/>
    <polygon points="610,105 613,125 590,105" fill="#8a2a10"/>
    <rect x="127" y="9" width="444" height="74" fill="#ec1f27" stroke="#ffe11a" stroke-width="4"/>
  </svg>
  <div class="ribbon-label">JAMBOREE</div>

  <div class="mascot-art" role="img" aria-label="Cartoon pig in overalls relaxing contentedly above the flames"></div>

  <section class="edition">
    <p class="edition-number">10th EVER</p>
    <p class="edition-tag">AN EATING EVENT</p>
  </section>

  <ul class="highlights">
    <li><svg class="star" viewBox="0 0 24 24"><polygon points="12,1 15,9 23,9 16.5,14 19,22 12,17 5,22 7.5,14 1,9 9,9"/></svg>Music &amp; Food</li>
    <li><svg class="star" viewBox="0 0 24 24"><polygon points="12,1 15,9 23,9 16.5,14 19,22 12,17 5,22 7.5,14 1,9 9,9"/></svg>Beers, Bands &amp; Bourbon</li>
    <li><svg class="star" viewBox="0 0 24 24"><polygon points="12,1 15,9 23,9 16.5,14 19,22 12,17 5,22 7.5,14 1,9 9,9"/></svg>Come to meet</li>
    <li class="indent">the TV Celebrity</li>
    <li class="indent">BBQ Pitmasters!</li>
  </ul>

  <p class="admission"><b>$5</b> Admission · <b>FREE</b> Music · <b>FREE</b> Parking</p>

  <aside class="beneficiary">
    <p class="beneficiary-label">FOR THE BENEFIT OF</p>
    <div class="beneficiary-name"><span class="mark"></span>Ridgeline Community Fund</div>
  </aside>

  <section class="host">
    <p class="host-label">HOSTED BY</p>
    <p class="host-name">Copperfield Hollow Distillery</p>
    <p>2817 Marlow Pike Ashby, KY 40198</p>
  </section>

  <svg class="date-badge" viewBox="0 0 232 222" aria-hidden="true">
    <polygon points="0,0 232,0 232,222 216,208 200,222 184,208 168,222 152,208 136,222 120,208 104,222 88,208 72,222 56,208 40,222 24,208 8,222 0,214" fill="#1b2f6b" stroke="#ffffff" stroke-width="3"/>
    <line x1="20" y1="80" x2="212" y2="80" stroke="#ffffff" stroke-width="1"/>
  </svg>
  <p class="badge-town">Ashby</p>
  <p class="badge-state">KENTUCKY</p>
  <p class="badge-dates">SEPTEMBER 4+5</p>
  <p class="badge-year">2020</p>

  <div class="footer-rule"></div>
  <p class="site-address">HARLANRIDGE<b>JAMBOREE</b>.COM</p>
</main>
</body>
</html>
```